Dental Savings Plan - Marcus Pelligrew DDS

We need a tri-fold brochure and 1 page flyer/poster for Dr. Marcus Pelligrew' dental office located on Maui, Hawaii. We are offering a new "Dental Savings Plan" to patients.
I have included 3 photos, along with the office logo. You do not have to use all photos if you do not want to. We want this to catch the eyes of patients, easy for them to read and understand, and to show them that this is a much better option than dental insurance.
Please use same Hawaiian theme and colors on the office website https://www.brightreefdental.com .

Please also include the following to promote this new plan:

Dental Services Include
• Professional Dental Cleanings (2 per benefit year)
• Perio Maintenance Cleanings (3 per benefit year) covered at 80%
• Radiographs as needed (1 set of X-rays per benefit year)
• Doctor Examinations (2 per benefit year)
• Ozone Treatment
• PRISM Amalgam Removal
• Additional limited/emergency exam (1 per benefit year)
• Cosmetic consultation
• 15% discount on all other services (including cosmetic procedures)
• 10% discount on implants and implant crowns

Advantages of the Dental Savings Plan
1. No deductibles
2. No waiting periods
3. No claims to file
4. No frequency limitations or exclusions
5. No yearly maximum benefits
6. No pre-authorization requirements
7. No pre-existing conditions limitations
8. State of the art facility and technology
9. Immediate enrollment
10. Highest quality of care for you and your Ohana

Annual Fee
$399 first family member/individual (equivalent to $33 per month)
$349 second family member (equivalent to $29 per month)
$249 each additional family member (equivalent to $20 per month)

Provisions of the Dental Savings Plan
• May not be combined with insurance plans, discounts or promotions
• This Dental Savings Plan is not an insurance plan, but a payment arrangement provided by Marcus Pelligrew DDS, and is not transferable to any other dental office or dental specialist
• Payment for services are due at the date of service
• This program is for you and is not transferable
• Benefits are provided for one year from the date the plan is purchased
• Must be paid in full when starting the plan
• No refunds will be provided for dues of the plan annual fee under any circumstances, including failure to schedule and maintain appointments
• If Paywell Finance is used to pay for the program and for services then only a 10% discount will be given
• To receive the full 15% discount on restorative treatment, you must schedule the appointment the day it is recommended. Any failed appointment results in the loss of the 15% discount.

Target Market(s)

Dental patients without dental insurance

Industry/Entity Type

Dental Clinic

Requirements
Must have
• My project must have the logo file to identify the dental office, Hawaiian theme, same colors as website, match style of website font, theme and colors, as well as, all the Dental Services, Advantages of the Dental Savings Plan, Annual Fee, and the Provisions of the Dental Savings Plan.

```html
<!DOCTYPE html>
<html lang="en">
<head>
<meta charset="utf-8">
<title>Dental Savings Plan – Marcus Pelligrew DDS</title>
<link rel="stylesheet" href="https://fonts.googleapis.com/css2?family=Fira+Sans+Condensed:ital,wght@0,400;0,600;1,600;1,700&family=Fira+Sans:ital,wght@0,400;0,700;1,700&display=swap">
<style>
:root{
  --blue:#1fa2dc;
  --blue-deep:#1689bd;
  --charcoal:#2b2d2c;
  --charcoal-soft:#343735;
  --ink:#ffffff;
  --muted:#d7dadb;
  --stage-top:#c8c8c8;
  --stage-bottom:#f1f1f1;
  --sky:#5fa8e0;
  --sea:#1fb8c9;
}
*{box-sizing:border-box;margin:0;padding:0}
html,body{width:1200px;height:1036px;overflow:hidden}
body{
  background:linear-gradient(var(--stage-top),var(--stage-bottom));
  font-family:"Fira Sans Condensed",sans-serif;
  color:var(--ink);
}
.spread{
  position:absolute;left:40px;width:1120px;height:476px;
  display:flex;box-shadow:0 10px 24px rgba(0,0,0,.25);
}
.spread--outside{top:24px}
.spread--inside{top:536px}
.panel{position:relative;width:373.33px;height:100%;overflow:hidden}
.panel--dark{background:linear-gradient(160deg,var(--charcoal-soft),var(--charcoal))}
.panel--blue{background:var(--blue)}
.photo{display:block;width:100%}

/* outside: fee panel */
.fee-photo{height:150px;background:linear-gradient(120deg,#e9d6cb,#f4f1ef 60%,#dfe4e8)}
.fee-body{padding:26px 34px}
.fee-title{font-family:"Fira Sans",sans-serif;font-style:italic;font-weight:700;color:var(--blue);font-size:30px;text-align:center;margin-bottom:22px}
.fee{margin-bottom:22px;font-family:"Fira Sans",sans-serif;font-size:15px;line-height:1.35}
.fee strong{font-style:italic;font-size:19px}
.fee small{display:block;font-style:italic;font-size:13.5px;color:var(--muted)}

/* outside: contact panel */
.brand{height:150px;background:#fff;display:flex;align-items:center;justify-content:center;gap:10px}
.brand-mark{width:22px;height:22px;border-radius:50%;background:var(--blue)}
.brand-name{font-family:"Fira Sans Condensed",sans-serif;font-weight:600;font-size:26px;color:var(--blue)}
.doctor-photo{height:150px;background:linear-gradient(90deg,#e6eaec,#c4ccd3 55%,#3d4a5c)}
.contact{height:176px;background:var(--blue);padding:18px 40px}
.contact-list{list-style:none;font-family:"Fira Sans",sans-serif;font-size:13px;line-height:1.9}
.contact-list li{display:flex;align-items:center;gap:10px}
.contact-list svg{flex:none}
.social{display:flex;gap:14px;justify-content:center;margin-top:14px}
.social span{width:30px;height:30px;border:2px solid #fff;border-radius:4px}

/* outside: cover panel */
.cover-photo{height:330px;background:linear-gradient(var(--sky) 0%,#a9d3f0 38%,var(--sea) 40%,#1597a8 100%)}
.cover-title{font-family:"Fira Sans",sans-serif;font-weight:700;font-size:32px;line-height:1.05;text-align:center;padding-top:30px}

/* inside */
.inside-body{padding:24px 26px 0 30px}
.inside-title{font-style:italic;font-weight:600;font-size:25px;line-height:1.15;margin-bottom:12px}
.services{list-style:none;font-size:13px;line-height:1.22}
.services li{margin-bottom:7px;padding-left:10px;position:relative}
.services li::before{content:"•";position:absolute;left:0}
.advantages{list-style:none;font-size:13px}
.advantages li{margin-bottom:12px}
.advantages .num{display:inline-block;width:20px}
.advantages .wrap{padding-left:20px;display:block;margin-top:5px}
.provisions{list-style:none;font-size:11px;line-height:1.2}
.provisions li{margin-bottom:8px;padding-left:10px;position:relative}
.provisions li::before{content:"•";position:absolute;left:0}
.badge{position:absolute;left:50%;bottom:14px;transform:translateX(-50%);width:48px;height:48px;border-radius:50%;background:var(--blue);display:flex;align-items:center;justify-content:center}
.badge--outline{background:none}
</style>
</head>
<body>

<section class="spread spread--outside">
  <article class="panel panel--dark fee-panel">
    <div class="photo fee-photo" role="img" aria-label="Photo of a patient smiling during a dental check-up"></div>
    <div class="fee-body">
      <h2 class="fee-title">Annual Fee</h2>
      <p class="fee"><strong>$399</strong> first family member/individual<small>(equivalent to $33 per month)</small></p>
      <p class="fee"><strong>$349</strong> second family member<small>(equivalent to $29 per month)</small></p>
      <p class="fee"><strong>$249</strong> each additional family member<small>(equivalent to $20 per month)</small></p>
    </div>
  </article>

  <article class="panel contact-panel">
    <div class="brand">
      <span class="brand-mark"></span>
      <span class="brand-name">Marcus Pelligrew DDS</span>
    </div>
    <div class="photo doctor-photo" role="img" aria-label="Photo of the dentist at his desk beside X-ray monitors"></div>
    <div class="contact">
      <ul class="contact-list">
        <li><svg width="14" height="14" viewBox="0 0 14 14"><circle cx="7" cy="7" r="6.2" fill="none" stroke="#fff"/><path d="M4.5 4h1.5l.6 1.6-.8.6a4 4 0 0 0 1.9 1.9l.6-.8 1.6.6V9.5A5.5 5.5 0 0 1 4.5 4z" fill="#fff"/></svg>808-555-0142</li>
        <li><svg width="14" height="14" viewBox="0 0 14 14"><circle cx="7" cy="7" r="6.2" fill="none" stroke="#fff"/><rect x="3.8" y="4.8" width="6.4" height="4.4" fill="none" stroke="#fff"/><path d="M3.8 4.8 7 7.4l3.2-2.6" fill="none" stroke="#fff"/></svg>hello@brightreefdental.com</li>
        <li><svg width="14" height="14" viewBox="0 0 14 14"><circle cx="7" cy="7" r="6.2" fill="none" stroke="#fff"/><circle cx="7" cy="7" r="3.5" fill="none" stroke="#fff"/><path d="M3.5 7h7M7 3.5c-1.5 2-1.5 5 0 7M7 3.5c1.5 2 1.5 5 0 7" fill="none" stroke="#fff" stroke-width=".8"/></svg>www.brightreefdental.com</li>
        <li><svg width="14" height="14" viewBox="0 0 14 14"><circle cx="7" cy="7" r="6.2" fill="none" stroke="#fff"/><path d="M7 11S4.5 8 4.5 6.2a2.5 2.5 0 0 1 5 0C9.5 8 7 11 7 11z" fill="#fff"/></svg>77 Coral Palm Ln #3, Kihei, HI 96753</li>
      </ul>
      <div class="social"><span></span><span></span><span></span></div>
    </div>
  </article>

  <article class="panel panel--dark cover-panel">
    <div class="photo cover-photo" role="img" aria-label="Photo of a palm tree over a turquoise tropical sea"></div>
    <h1 class="cover-title">Dental<br>Savings<br>Plan</h1>
  </article>
</section>

<section class="spread spread--inside">
  <article class="panel panel--dark">
    <div class="inside-body">
      <h2 class="inside-title">Dental Services Include</h2>
      <ul class="services">
        <li>Professional Dental Cleanings<br>(2 per benefit year)</li>
        <li>Perio Maintenance Cleanings<br>(3 per benefit year) covered at 80%</li>
        <li>Radiographs as needed<br>(1 set of X-rays per benefit year)</li>
        <li>Doctor Examinations<br>(2 per benefit year)</li>
        <li>Ozone Treatment</li>
        <li>PRISM Amalgam Removal</li>
        <li>Additional limited/emergency exam<br>(1 per benefit year)</li>
        <li>Cosmetic consultation</li>
        <li>15% discount on all other services<br>(including cosmetic procedures)</li>
        <li>10% discount on implants and implant crowns</li>
      </ul>
    </div>
    <span class="badge"><svg width="24" height="28" viewBox="0 0 24 28"><path d="M6 2c3 0 4 1.5 6 1.5S15 2 18 2c3.5 0 5 3 4.5 7-.4 3-2 5-2.5 9-.4 3.5-1 7.5-3 7.5s-2-6-5-6-3 6-5 6-2.6-4-3-7.5C3.5 14 2 12 1.5 9 1 5 2.5 2 6 2z" fill="none" stroke="#fff" stroke-width="1.6"/></svg></span>
  </article>

  <article class="panel panel--blue">
    <div class="inside-body">
      <h2 class="inside-title">Advantages of the<br>Dental Savings Plan</h2>
      <ol class="advantages">
        <li><span class="num">1.</span>No deductibles</li>
        <li><span class="num">2.</span>No waiting periods</li>
        <li><span class="num">3.</span>No claims to file</li>
        <li><span class="num">4.</span>No frequency limitations or exclusions</li>
        <li><span class="num">5.</span>No yearly maximum benefits</li>
        <li><span class="num">6.</span>No pre-authorization requirements</li>
        <li><span class="num">7.</span>No pre-existing conditions limitations</li>
        <li><span class="num">8.</span>State of the art facility and technology</li>
        <li><span class="num">9.</span>Immediate enrollment</li>
        <li><span class="num">10.</span>Highest quality of care for you<span class="wrap">and your Ohana</span></li>
      </ol>
    </div>
    <span class="badge badge--outline"><svg width="36" height="40" viewBox="0 0 24 28"><path d="M6 2c3 0 4 1.5 6 1.5S15 2 18 2c3.5 0 5 3 4.5 7-.4 3-2 5-2.5 9-.4 3.5-1 7.5-3 7.5s-2-6-5-6-3 6-5 6-2.6-4-3-7.5C3.5 14 2 12 1.5 9 1 5 2.5 2 6 2z" fill="none" stroke="#fff" stroke-width="1.3"/></svg></span>
  </article>

  <article class="panel panel--dark">
    <div class="inside-body">
      <h2 class="inside-title">Provisions of the<br>Dental Savings Plan</h2>
      <ul class="provisions">
        <li>May not be combined with insurance plans, discounts or promotions</li>
        <li>This Dental Savings Plan is not an insurance plan, but a payment arrangement provided by Marcus Pelligrew DDS, and is not transferable to any other dental office or dental specialist</li>
        <li>Payment for services are due at the date of service</li>
        <li>This program is for you and is not transferable</li>
        <li>Benefits are provided for one year from the date the plan is purchased</li>
        <li>Must be paid in full when starting the plan</li>
        <li>No refunds will be provided for dues of the plan annual fee under any circumstances, including failure to schedule and maintain appointments</li>
        <li>If Paywell Finance is used to pay for the program and for services then only a 10% discount will be given</li>
        <li>To receive the full 15% discount on restorative treatment, you must schedule the appointment the day it is recommended. Any failed appointment results in the loss of the 15% discount.</li>
      </ul>
    </div>
    <span class="badge"><svg width="24" height="28" viewBox="0 0 24 28"><path d="M6 2c3 0 4 1.5 6 1.5S15 2 18 2c3.5 0 5 3 4.5 7-.4 3-2 5-2.5 9-.4 3.5-1 7.5-3 7.5s-2-6-5-6-3 6-5 6-2.6-4-3-7.5C3.5 14 2 12 1.5 9 1 5 2.5 2 6 2z" fill="none" stroke="#fff" stroke-width="1.6"/></svg></span>
  </article>
</section>

</body>
</html>
```